K7 Digital Stationery Design Project

We are looking to have stationary designs created for our company branding materials. We are looking for the following to be created.
1. Business Cards (front & back)
2. Letterhead
3. Envelopes #10
We are a new web design, development and marketing firm. Primary color scheme is desired to be blue/grey/white. This web start-up is owned and operated by individuals with 15+ years experience each in the industry so should not look as though it is a start-up by young/inexperienced individuals.
We build website & custom applications/software. In addition we provide the full spectrum of web marketing solutions including SEO, PPC, Social Media, Branding, Content Marketing and PR.
Please let us know if you have any questions. Looking forward to seeing all the amazing design ideas.
Attached is our logo.
Thanks!
Target Market(s)
Company will be nearly 100% business to business sales. Looking to work with companies that are already established, with a website, who want to take their website and/or online marketing efforts to the next level.
Industry/Entity Type
Marketing
Look and feel

```html
<!DOCTYPE html>
<html lang="en">
<head>
<meta charset="utf-8">
<title>K7 Digital – Business Card Set</title>
<link rel="stylesheet" href="https://fonts.googleapis.com/css2?family=Jost:wght@400;500;700&family=PT+Sans&display=swap">
<style>
  :root {
    --stage: #7a5640;
    --label: #111111;
    --card-white: #ffffff;
    --ink: #333333;
    --ink-soft: #555555;
    --blue-light: #17a8dc;
    --blue: #1a86c8;
    --blue-deep: #1670b8;
    --night: #2b2d30;
    --night-deep: #0e0f10;
    --white: #ffffff;
  }
  * { margin: 0; padding: 0; box-sizing: border-box; }
  html, body { width: 1200px; height: 788px; overflow: hidden; }
  body {
    background: var(--stage);
    font-family: "Jost", "Futura", sans-serif;
    position: relative;
  }
  .set-label {
    position: absolute;
    font-family: "PT Sans", "Myriad Pro", sans-serif;
    font-size: 22px;
    color: var(--label);
    transform: translateX(-50%);
    white-space: nowrap;
  }
  .card {
    position: absolute;
    width: 526px;
    height: 300px;
    border-radius: 22px;
    overflow: hidden;
  }
  .card > * { position: absolute; }
  .card--front { left: 55px; top: 73px; background: var(--card-white); }
  .card--back-white { left: 622px; top: 74px; background: var(--card-white); }
  .card--back-blue { left: 53px; top: 445px; background: linear-gradient(100deg, var(--blue-light) 0%, var(--blue) 55%, var(--blue-deep) 100%); }
  .card--back-dark { left: 622px; top: 445px; background: radial-gradient(ellipse at 50% 35%, var(--night) 0%, var(--night-deep) 80%); }

  .swoosh { left: 0; top: 0; width: 526px; height: 300px; }

  .brand-dot { border-radius: 50%; }
  .brand-name { font-weight: 700; letter-spacing: 0.2px; white-space: nowrap; line-height: 1; }
  .tagline { font-weight: 500; white-space: nowrap; line-height: 1; }
  .web { white-space: nowrap; line-height: 1; }

  /* Front */
  .card--front .brand-dot { left: 100px; top: 62px; width: 58px; height: 58px; background: var(--blue); }
  .card--front .brand-name { left: 24px; top: 158px; font-size: 27px; color: var(--ink); }
  .card--front .tagline { left: 24px; top: 184px; font-size: 10.5px; color: var(--ink); }
  .holder { left: 24px; top: 218px; font-size: 17px; font-weight: 700; color: var(--ink); white-space: nowrap; }
  .holder .role { font-size: 13px; font-weight: 400; color: var(--ink-soft); }
  .address { left: 26px; top: 265px; font-size: 12.5px; color: var(--ink-soft); white-space: nowrap; }
  .divider { left: 247px; top: 217px; width: 1px; height: 62px; background: #888; }
  .contacts { left: 263px; top: 215px; list-style: none; font-size: 12.5px; color: var(--ink-soft); line-height: 17.5px; white-space: nowrap; }
  .contacts b { font-style: italic; color: var(--ink); }

  /* Back 1 */
  .card--back-white .brand-dot { left: 233px; top: 42px; width: 60px; height: 60px; background: var(--blue); }
  .card--back-white .brand-name { left: 0; width: 100%; text-align: center; top: 190px; font-size: 37px; color: var(--ink); }
  .card--back-white .tagline { left: 0; width: 100%; text-align: center; top: 226px; font-size: 14px; color: var(--ink); }
  .card--back-white .web { left: 0; width: 100%; text-align: center; top: 262px; font-size: 16px; letter-spacing: 5px; color: var(--ink); }

  /* Back 2 */
  .card--back-blue .brand-dot { left: 60px; top: 80px; width: 110px; height: 110px; background: var(--white); }
  .card--back-blue .brand-name { left: 177px; top: 123px; font-size: 42px; color: var(--white); }
  .card--back-blue .tagline { left: 177px; top: 166px; font-size: 16px; color: var(--white); }
  .card--back-blue .web { right: 24px; top: 266px; font-size: 16px; color: var(--white); }

  /* Back 3 */
  .card--back-dark .brand-dot { left: 233px; top: 45px; width: 60px; height: 60px; background: var(--blue-light); }
  .card--back-dark .brand-name { left: 0; width: 100%; text-align: center; top: 196px; font-size: 34px; color: var(--white); }
  .card--back-dark .tagline { left: 0; width: 100%; text-align: center; top: 229px; font-size: 13px; color: var(--white); }
  .card--back-dark .web { left: 0; width: 100%; text-align: center; top: 266px; font-size: 16px; letter-spacing: 5px; color: var(--white); }
</style>
</head>
<body>

  <div class="set-label" style="left:320px; top:34px;">Front</div>
  <div class="set-label" style="left:895px; top:34px;">Back - 1</div>
  <div class="set-label" style="left:325px; top:404px;">Back - 2</div>
  <div class="set-label" style="left:897px; top:404px;">Back - 3</div>

  <section class="card card--front">
    <svg class="swoosh" viewBox="0 0 526 300" aria-hidden="true">
      <defs>
        <linearGradient id="swoosh-fill" x1="0" y1="0" x2="1" y2="1">
          <stop offset="0" stop-color="#0f9ad6"/>
          <stop offset="1" stop-color="#1a7cc4"/>
        </linearGradient>
      </defs>
      <path d="M395,0 C455,25 500,80 512,150" fill="none" stroke="#1a86c8" stroke-width="11"/>
      <path d="M440,0 L526,0 L526,300 L442,300 C520,220 530,90 440,0 Z" fill="url(#swoosh-fill)"/>
    </svg>
    <div class="brand-dot"></div>
    <div class="brand-name">K7 DIGITAL</div>
    <div class="tagline">Web Design, Development and Marketing</div>
    <div class="holder">Your Name, <span class="role">Designation</span></div>
    <div class="address">123 Abc Street, 0000 city, country</div>
    <div class="divider"></div>
    <ul class="contacts">
      <li><b>c</b> : +12 345 67 8910</li>
      <li><b>p</b> : +12 345 67 8910</li>
      <li><b>e</b> : name@website.com</li>
      <li><b>w</b> : www.website.com</li>
    </ul>
  </section>

  <section class="card card--back-white">
    <div class="brand-dot"></div>
    <div class="brand-name">K7 DIGITAL</div>
    <div class="tagline">Web Design, Development and Marketing</div>
    <div class="web">www.website.com</div>
  </section>

  <section class="card card--back-blue">
    <div class="brand-dot"></div>
    <div class="brand-name">K7 DIGITAL</div>
    <div class="tagline">Web Design, Development and Marketing</div>
    <div class="web">www.website.com</div>
  </section>

  <section class="card card--back-dark">
    <div class="brand-dot"></div>
    <div class="brand-name">K7 DIGITAL</div>
    <div class="tagline">Web Design, Development and Marketing</div>
    <div class="web">www.website.com</div>
  </section>

</body>
</html>
```